Generic fund comparison

We need a power point template to be used for presentation decks and proposals to clients and prospects. We are an independent Registered Investment Advisor in Pittsburgh Pennsylvania.
Our services include family office, alternative investments, investment management, financial planning and consulting.
We would like to see designs that use the color green and grey as they are part of our logo and brand image. The final design should communicate our guiding principles: 'educate, plan, implement, adapt'

```html
<!DOCTYPE html>
<html lang="en">
<head>
<meta charset="utf-8">
<title>Ventara – Presentation Template</title>
<link href="https://fonts.googleapis.com/css2?family=Raleway:wght@400;500;600;700&family=Open+Sans:wght@400;600;700&display=swap" rel="stylesheet">
<style>
:root{
  --green:#8dc63f;
  --green-dark:#6fa52a;
  --green-pale:#c6efce;
  --grey:#7a7772;
  --grey-dark:#5f5c58;
  --ink:#222;
  --muted:#8a8a8a;
  --canvas:#e7e7e7;
  --pink:#f4c7c3;
  --white:#fff;
}
*{box-sizing:border-box;margin:0;padding:0}
html,body{width:1200px;height:3386px;overflow:hidden;background:var(--canvas)}
body{font-family:"Raleway",sans-serif;color:var(--ink)}
.canvas{position:relative;width:1200px;height:3386px;overflow:hidden;background:var(--canvas)}
.slide{position:absolute;width:585px;height:329px;background:var(--white);overflow:hidden}
.col-l{left:10px}.col-r{left:605px}
.r1{top:10px}.r2{top:347px}.r3{top:684px}.r4{top:1021px}.r5{top:1358px}
.r6{top:1695px}.r7{top:2032px}.r8{top:2369px}.r9{top:2706px}.r10{top:3043px}
.abs{position:absolute}
.bg-grey{background:var(--grey)}
.bg-green{background:var(--green)}

/* brand */
.brand{position:absolute;display:flex;flex-direction:column;align-items:center;gap:6px}
.brand.left{align-items:flex-start}
.brand-mark{width:14px;height:14px;background:var(--green)}
.brand-name{font-family:"Raleway",sans-serif;font-weight:600;font-size:13px;letter-spacing:.5px;color:var(--grey)}
.brand.on-dark .brand-name{color:var(--white)}

/* cover titles */
.cover-title{position:absolute;font-weight:600;font-size:23px;line-height:26px}
.cover-title.white{color:var(--white)}
.cover-title.grey{color:var(--grey)}
.cover-title.center{left:0;right:0;text-align:center;font-size:28px;line-height:31px}
.cover-date{display:block;font-weight:400;font-size:11px;line-height:16px;margin-top:2px}
.bar-top{position:absolute;left:0;right:0;top:0;height:7px;background:var(--green)}
.bar-bottom{position:absolute;left:0;right:0;bottom:0;height:10px;background:var(--green)}
.growth{position:absolute;left:0;top:0;width:585px;height:329px}

/* content slide chrome */
.corner-mark{position:absolute;left:7px;top:7px;width:13px;height:13px;background:var(--green)}
.page-no{position:absolute;left:7px;bottom:7px;width:14px;height:14px;background:var(--green);color:var(--white);font:600 6px "Open Sans",sans-serif;display:flex;align-items:center;justify-content:center}
.side-note{position:absolute;left:15px;top:164px;transform:translate(-50%,-50%) rotate(-90deg);white-space:nowrap;font:400 5.5px "Open Sans",sans-serif;color:#aaa}
.slide-title{position:absolute;left:46px;top:22px;font-weight:700;font-size:20px;color:var(--ink)}
.title-rule{position:absolute;left:46px;top:54px;width:30px;height:3px;background:var(--green)}
.footnote{position:absolute;font:400 6px "Open Sans",sans-serif;color:var(--muted)}

/* agenda */
.agenda-title{position:absolute;left:71px;top:114px;font-weight:700;font-size:21px;line-height:27px}
.agenda-sub{position:absolute;left:71px;top:200px;font-weight:700;font-size:10px;color:var(--green)}
.agenda-list{position:absolute;left:328px;top:57px;width:204px;list-style:none}
.agenda-list li{display:flex;height:23.4px;align-items:center;border-bottom:1px solid #e6e6e6;font:400 10px "Open Sans",sans-serif;color:#444}
.agenda-list .num{width:36px;color:#b9dc8a}

/* text slide */
.text-title{position:absolute;left:49px;top:44px;font-weight:700;font-size:25px}
.text-body{position:absolute;left:49px;top:102px;width:492px;font:400 6.6px/8.6px "Open Sans",sans-serif;color:#444;text-align:justify}
.text-body p{margin-bottom:8.6px}

/* pie */
.pie-title{position:absolute;left:289px;top:110px;font-weight:700;font-size:27px}
.pie-lead{position:absolute;left:289px;top:160px;font-weight:500;font-size:11px;color:var(--green)}
.pie-copy{position:absolute;left:289px;top:178px;width:232px;font:400 9.5px/12px "Open Sans",sans-serif;color:#444}

/* tables */
.data-svg{position:absolute;left:0;top:0;width:585px;height:329px}
.svg-text{font-family:"Open Sans",sans-serif}

/* disclaimer */
.disc-title{position:absolute;left:46px;top:40px;font-weight:700;font-size:30px}
.disc-body{position:absolute;left:46px;top:92px;width:497px;font:400 7px/13.1px "Open Sans",sans-serif;color:#444;text-align:justify}
</style>
</head>
<body>
<main class="canvas">

<!-- Cover A: grey block, green square -->
<section class="slide col-l r1">
  <div class="abs bg-grey" style="left:0;top:0;width:585px;height:252px"></div>
  <h1 class="cover-title white" style="left:46px;top:92px">Independent<br>Financial Advisory<br>Services Tailored To<br>Your Goals<span class="cover-date">ABC, XYZ – April 2021</span></h1>
  <div class="abs bg-green" style="left:355px;top:49px;width:164px;height:164px"></div>
  <div class="brand" style="left:0;right:0;top:270px"><span class="brand-mark"></span><span class="brand-name">VENTARA</span></div>
</section>

<!-- Cover B: white, green square right -->
<section class="slide col-r r1">
  <div class="brand left" style="left:55px;top:58px"><span class="brand-mark"></span><span class="brand-name">VENTARA</span></div>
  <h1 class="cover-title grey" style="left:55px;top:125px">Independent<br>Financial Advisory<br>Services Tailored<br>To Your Goals<span class="cover-date" style="color:var(--muted)">ABC, XYZ – April 2021</span></h1>
  <div class="abs bg-green" style="left:302px;top:49px;width:240px;height:237px"></div>
</section>

<!-- Cover C: green field, white square -->
<section class="slide col-l r2 bg-green">
  <h1 class="cover-title white" style="left:37px;top:123px">Independent<br>Financial Advisory<br>Services Tailored<br>To Your Goals<span class="cover-date">ABC, XYZ – April 2021</span></h1>
  <div class="abs" style="left:303px;top:51px;width:232px;height:231px;background:var(--white)"></div>
</section>

<!-- Cover D: grey, centred -->
<section class="slide col-r r2 bg-grey">
  <div class="bar-top"></div>
  <div class="brand on-dark" style="left:0;right:0;top:64px"><span class="brand-mark"></span><span class="brand-name">VENTARA</span></div>
  <h1 class="cover-title white center" style="top:136px">Independent Financial<br>Advisory Services<br>Tailored To Your Goals<span class="cover-date">ABC, XYZ – April 2021</span></h1>
  <div class="bar-bottom"></div>
</section>

<!-- Cover E: grey, centred -->
<section class="slide col-l r3 bg-grey">
  <div class="brand on-dark" style="left:0;right:0;top:58px"><span class="brand-mark"></span><span class="brand-name">VENTARA</span></div>
  <h1 class="cover-title white center" style="top:128px">Independent Financial<br>Advisory Services<br>Tailored To Your Goals<span class="cover-date">ABC, XYZ – April 2021</span></h1>
  <div class="bar-bottom"></div>
</section>

<!-- Cover F: growth curve, white -->
<section class="slide col-r r3">
  <div class="brand left" style="left:40px;top:62px"><span class="brand-mark"></span><span class="brand-name">VENTARA</span></div>
  <h1 class="cover-title grey" style="left:38px;top:110px;font-size:26px;line-height:29px">Independent Financial<br>Advisory Services<br>Tailored To Your Goals<span class="cover-date" style="color:var(--muted)">ABC, XYZ – April 2021</span></h1>
  <svg class="growth" viewBox="0 0 585 329" aria-hidden="true">
    <polyline points="59,284 116,284 176,284 238,284 301,279 353,262 402,231 447,183 493,112 526,42" fill="none" stroke="#8dc63f" stroke-width="4"/>
    <g fill="#8dc63f"><rect x="54" y="279" width="10" height="10"/><rect x="111" y="279" width="10" height="10"/><rect x="171" y="279" width="10" height="10"/><rect x="233" y="279" width="10" height="10"/><rect x="294" y="272" width="14" height="14"/><rect x="345" y="254" width="16" height="16"/><rect x="393" y="222" width="18" height="18"/><rect x="437" y="173" width="20" height="20"/><rect x="482" y="101" width="22" height="22"/><rect x="513" y="29" width="26" height="26"/></g>
  </svg>
  <div class="bar-bottom"></div>
</section>

<!-- Cover G: growth curve, white -->
<section class="slide col-l r4">
  <div class="bar-top"></div>
  <div class="brand left" style="left:40px;top:62px"><span class="brand-mark"></span><span class="brand-name">VENTARA</span></div>
  <h1 class="cover-title grey" style="left:38px;top:110px;font-size:26px;line-height:29px">Independent Financial<br>Advisory Services<br>Tailored To Your Goals<span class="cover-date" style="color:var(--muted)">ABC, XYZ – April 2021</span></h1>
  <svg class="growth" viewBox="0 0 585 329" aria-hidden="true">
    <polyline points="59,284 116,284 176,284 238,284 301,279 353,262 402,231 447,183 493,112 526,42" fill="none" stroke="#8dc63f" stroke-width="4"/>
    <g fill="#8dc63f"><rect x="54" y="279" width="10" height="10"/><rect x="111" y="279" width="10" height="10"/><rect x="171" y="279" width="10" height="10"/><rect x="233" y="279" width="10" height="10"/><rect x="294" y="272" width="14" height="14"/><rect x="345" y="254" width="16" height="16"/><rect x="393" y="222" width="18" height="18"/><rect x="437" y="173" width="20" height="20"/><rect x="482" y="101" width="22" height="22"/><rect x="513" y="29" width="26" height="26"/></g>
  </svg>
  <div class="bar-bottom"></div>
</section>

<!-- Cover H: growth curve, grey -->
<section class="slide col-r r4 bg-grey">
  <div class="bar-top"></div>
  <div class="brand left on-dark" style="left:40px;top:58px"><span class="brand-mark"></span><span class="brand-name">VENTARA</span></div>
  <h1 class="cover-title white" style="left:38px;top:104px;font-size:26px;line-height:29px">Independent Financial<br>Advisory Services<br>Tailored To Your Goals<span class="cover-date">ABC, XYZ – April 2021</span></h1>
  <svg class="growth" viewBox="0 0 585 329" aria-hidden="true">
    <polyline points="50,277 107,277 167,277 229,277 292,272 344,255 393,224 438,176 484,105 517,35" fill="none" stroke="#8dc63f" stroke-width="4"/>
    <g fill="#8dc63f"><rect x="45" y="272" width="10" height="10"/><rect x="102" y="272" width="10" height="10"/><rect x="162" y="272" width="10" height="10"/><rect x="224" y="272" width="10" height="10"/><rect x="285" y="265" width="14" height="14"/><rect x="336" y="247" width="16" height="16"/><rect x="384" y="215" width="18" height="18"/><rect x="428" y="166" width="20" height="20"/><rect x="473" y="94" width="22" height="22"/><rect x="504" y="22" width="26" height="26"/></g>
  </svg>
  <div class="bar-bottom"></div>
</section>

<!-- Agenda -->
<section class="slide col-l r5">
  <span class="corner-mark"></span><span class="side-note">Private and Confidential – Not for Distribution</span><span class="page-no">9</span>
  <h2 class="agenda-title">Here Goes<br>Title Of Your<br>Agenda</h2>
  <p class="agenda-sub">Here Goes A Short Subtitle</p>
  <ol class="agenda-list">
    <li><span class="num">i.</span>Introduction</li>
    <li><span class="num">ii.</span>About Us</li>
    <li><span class="num">iii.</span>Welcome Message</li>
    <li><span class="num">iv.</span>Company Profile</li>
    <li><span class="num">v.</span>Team</li>
    <li><span class="num">vi.</span>Team Group</li>
    <li><span class="num">vii.</span>Portfolio</li>
    <li><span class="num">viii.</span>Info graphic</li>
    <li><span class="num">ix.</span>Contact Us</li>
  </ol>
</section>

<!-- Blank layout -->
<section class="slide col-r r5">
  <span class="corner-mark"></span><span class="side-note">Private and Confidential – Not for Distribution</span><span class="page-no">10</span>
</section>

<!-- Simple text -->
<section class="slide col-l r6">
  <span class="corner-mark"></span><span class="side-note">Private and Confidential – Not for Distribution</span><span class="page-no">11</span>
  <h2 class="text-title">Simple Text Slide</h2>
  <div class="text-body">
    <p>Lorem ipsum dolor sit amet, consectetur adipiscing elit, sed do eiusmod tempor incididunt ut labore et dolore magna aliqua. Lorem ipsum dolor sit amet, consectetur adipiscing elit, sed do eiusmod tempor incididunt ut labore et dolore magna aliqua. Ut enim ad minim veniam, quis nostrud exercitation ullamco laboris nisi ut aliquip.</p>
    <p>Lorem ipsum dolor sit amet, consectetur adipiscing elit, sed do eiusmod tempor incididunt ut labore et dolore magna aliqua. Lorem ipsum dolor sit amet, consectetur adipiscing elit, sed do eiusmod tempor incididunt ut labore et dolore magna aliqua. Ut enim ad minim veniam, quis nostrud exercitation ullamco laboris nisi ut aliquip. Lorem ipsum dolor sit amet, consectetur adipiscing elit, sed do eiusmod tempor incididunt ut labore et dolore magna aliqua. Lorem ipsum dolor sit amet, consectetur adipiscing elit. Ut enim ad minim veniam, quis nostrud exercitation ullamco laboris nisi ut aliquip.</p>
    <p>Lorem ipsum dolor sit amet, consectetur adipiscing elit, sed do eiusmod tempor incididunt ut labore et dolore magna aliqua. Lorem ipsum dolor sit amet, consectetur adipiscing elit, sed do eiusmod tempor incididunt ut labore et dolore magna aliqua. Ut enim ad minim veniam, quis nostrud exercitation ullamco laboris nisi ut aliquip. Lorem ipsum dolor sit amet, consectetur adipiscing elit, sed do eiusmod tempor incididunt ut labore et dolore magna aliqua. Ut enim ad minim veniam, quis nostrud exercitation ullamco laboris nisi ut aliquip.</p>
    <p>Lorem ipsum dolor sit amet, consectetur adipiscing elit, sed do eiusmod tempor incididunt ut labore et dolore magna aliqua. Lorem ipsum dolor sit amet, consectetur adipiscing elit, sed do eiusmod tempor incididunt ut labore et dolore magna aliqua. Ut enim ad minim veniam, quis nostrud exercitation ullamco laboris nisi ut aliquip.</p>
  </div>
</section>

<!-- Pie chart -->
<section class="slide col-r r6">
  <span class="corner-mark"></span><span class="side-note">Private and Confidential – Not for Distribution</span><span class="page-no">12</span>
  <svg class="data-svg" viewBox="0 0 585 329" role="img" aria-label="Pie chart: 64% 1st Qtr, 25% 2nd Qtr, 11% 3rd Qtr">
    <g transform="translate(0,12) scale(1,0.82)">
      <ellipse cx="147" cy="222" rx="92" ry="92" fill="#3d3d3d"/>
      <path d="M147,222 L147,130 A92,92 0 1 1 76.1,280.6 Z" fill="#5f8f22"/>
      <path d="M147,213 L147,121 A92,92 0 1 1 76.1,271.6 Z" fill="#8dc63f"/>
      <path d="M147,213 L76.1,271.6 A92,92 0 0 1 88.4,142.1 Z" fill="#7a7772"/>
      <path d="M147,213 L88.4,142.1 A92,92 0 0 1 147,121 Z" fill="#111"/>
    </g>
    <g class="svg-text" font-size="10" font-weight="700" fill="#fff" text-anchor="middle">
      <text x="171" y="185">64%</text><text x="92" y="160">25%</text><text x="129" y="118">11%</text>
    </g>
    <g class="svg-text" font-size="6" fill="#777">
      <rect x="100" y="274" width="5" height="5" fill="#8dc63f"/><text x="108" y="279">1st Qtr</text>
      <rect x="135" y="274" width="5" height="5" fill="#7a7772"/><text x="143" y="279">2nd Qtr</text>
      <rect x="172" y="274" width="5" height="5" fill="#111"/><text x="180" y="279">3rd Qtr</text>
    </g>
  </svg>
  <h2 class="pie-title">Pie Chart</h2>
  <p class="pie-lead">Lorem ipsum dolor sit amet</p>
  <p class="pie-copy">Lorem ipsum dolor sit amet, consectetur adipiscing elit, sed do eiusmod tempor incididunt ut labore et dolore magna aliqua. Lorem ipsum dolor sit amet, consectetur adipiscing elit. Lorem ipsum dolor sit amet, consectetur adipiscing elit, sed do eiusmod tempor incididunt ut labore et dolore magna aliqua.</p>
</section>

<!-- Growth of $1,000 -->
<section class="slide col-l r7">
  <span class="corner-mark"></span><span class="side-note">Private and Confidential – Not for Distribution</span><span class="page-no">13</span>
  <h2 class="slide-title">ABC, XYZ – Growth of $1,000 vs Benchmark*</h2>
  <svg class="data-svg" viewBox="0 0 585 329" role="img" aria-label="Line chart of growth of $1,000 for ABC, XYZ against benchmarks">
    <g stroke="#eee" stroke-width="1"><line x1="105" y1="83" x2="508" y2="83"/><line x1="105" y1="108" x2="508" y2="108"/><line x1="105" y1="133" x2="508" y2="133"/><line x1="105" y1="158" x2="508" y2="158"/><line x1="105" y1="183" x2="508" y2="183"/><line x1="105" y1="208" x2="508" y2="208"/><line x1="105" y1="233" x2="508" y2="233"/><line x1="105" y1="258" x2="508" y2="258"/></g>
    <g class="svg-text" font-size="5.5" fill="#777" text-anchor="end"><text x="100" y="85">$3,500</text><text x="100" y="110">$3,000</text><text x="100" y="135">$2,500</text><text x="100" y="160">$2,000</text><text x="100" y="185">$1,500</text><text x="100" y="210">$1,000</text><text x="100" y="235">$500</text><text x="100" y="260">$-</text></g>
    <polyline fill="none" stroke="#f2c12e" stroke-width="1.4" points="105,207 126,208 147,207 168,207 190,206 211,205 232,205 253,204 274,203 296,202 317,201 338,200 359,198 380,197 402,195 423,193 444,191 465,189 486,187 508,185"/>
    <polyline fill="none" stroke="#e98a2c" stroke-width="1.4" points="105,207 126,207 147,205 168,204 190,203 211,201 232,200 253,198 274,197 296,195 317,193 338,191 359,189 380,187 402,184 423,181 444,176 465,172 486,166 508,159"/>
    <polyline fill="none" stroke="#2f6fb7" stroke-width="1.4" points="105,207 126,206 147,204 168,203 190,201 211,199 232,197 253,195 274,193 296,191 317,188 338,186 359,183 380,180 402,176 423,172 444,166 465,160 486,152 508,146"/>
    <polyline fill="none" stroke="#8dc63f" stroke-width="1.4" points="105,207 126,206 147,203 168,201 190,199 211,197 232,194 253,192 274,189 296,186 317,182 338,178 359,175 380,170 402,163 423,156 444,146 465,133 486,115 508,96"/>
    <g class="svg-text" font-size="5.5" fill="#777">
      <text x="470" y="88">ABC $3,228</text><text x="428" y="142">Hedge Funds 50/50 $2,573</text><text x="450" y="154">Benchmark $2,158</text><text x="470" y="197">XYZ $1,971</text>
    </g>
    <g class="svg-text" font-size="4.5" fill="#999">
      <text transform="translate(110,275) rotate(-90)">Jan-10</text><text transform="translate(147,275) rotate(-90)">Jan-11</text><text transform="translate(190,275) rotate(-90)">Jan-12</text><text transform="translate(232,275) rotate(-90)">Jan-13</text><text transform="translate(274,275) rotate(-90)">Jan-14</text><text transform="translate(317,275) rotate(-90)">Jan-15</text><text transform="translate(359,275) rotate(-90)">Jan-16</text><text transform="translate(402,275) rotate(-90)">Jan-17</text><text transform="translate(444,275) rotate(-90)">Jan-18</text><text transform="translate(486,275) rotate(-90)">Jan-19</text><text transform="translate(508,275) rotate(-90)">Jan-20</text>
    </g>
  </svg>
  <p class="footnote" style="left:80px;top:298px">Benchmark = 45% xxxxxxxx, 15% yyyyyyyy, 40% zzzzzzzz</p>
</section>

<!-- Annual returns table -->
<section class="slide col-r r7">
  <span class="corner-mark"></span><span class="side-note">Private and Confidential – Not for Distribution</span><span class="page-no">14</span>
  <h2 class="slide-title">ABC, XYZ – Annual Returns vs Benchmark*</h2>
  <svg class="data-svg" viewBox="0 0 585 329" role="img" aria-label="Table of annual returns 2011 to YTD 2021">
    <text class="svg-text" x="149" y="96" font-size="8" font-weight="700" fill="#222">LAKEVIEW</text>
    <rect x="114" y="99" width="418" height="10" fill="#8dc63f"/>
    <rect x="114" y="109" width="418" height="10" fill="#b3b3b3"/>
    <g class="svg-text" font-size="5.5" font-weight="700" fill="#fff" text-anchor="middle">
      <text x="166" y="106">60/40</text><text x="271" y="106">Harbor Point</text><text x="375" y="106">Delta Crest</text><text x="480" y="106">50/50</text>
      <text x="166" y="116">BENCHMARK</text><text x="271" y="116">BAY</text><text x="375" y="116">COMPOSITE</text><text x="480" y="116">HEDGE FUNDS</text>
    </g>
    <rect x="114" y="120" width="418" height="148" fill="#c6efce"/>
    <rect x="114" y="173" width="104" height="13.5" fill="#f4c7c3"/>
    <rect x="218" y="173" width="105" height="13.5" fill="#f4c7c3"/>
    <rect x="114" y="186.5" width="104" height="13.5" fill="#f4c7c3"/>
    <rect x="218" y="186.5" width="105" height="13.5" fill="#f4c7c3"/>
    <rect x="114" y="227" width="104" height="13.5" fill="#f4c7c3"/>
    <g stroke="#fff" stroke-width="1"><line x1="218" y1="120" x2="218" y2="268"/><line x1="323" y1="120" x2="323" y2="268"/><line x1="427" y1="120" x2="427" y2="268"/></g>
    <g class="svg-text" font-size="8" fill="#222">
      <g><text x="66" y="130">2011</text><text x="66" y="143.5">2012</text><text x="66" y="157">2013</text><text x="66" y="170.5">2014</text><text x="66" y="184">2015</text><text x="66" y="197.5">2016</text><text x="66" y="211">2017</text><text x="66" y="224.5">2018</text><text x="66" y="238">2019</text><text x="66" y="251.5">2020</text><text x="66" y="265">YTD 2021</text></g>
      <g text-anchor="middle">
        <text x="166" y="130">0.6%</text><text x="271" y="130">4.6%</text><text x="375" y="130">4.8%</text><text x="480" y="130">4.7%</text>
        <text x="166" y="143.5">11.3%</text><text x="271" y="143.5">10.5%</text><text x="375" y="143.5">14.5%</text><text x="480" y="143.5">12.5%</text>
        <text x="166" y="157">16.0%</text><text x="271" y="157">8.2%</text><text x="375" y="157">12.3%</text><text x="480" y="157">10.2%</text>
        <text x="166" y="170.5">6.1%</text><text x="271" y="170.5">-2.5%</text><text x="375" y="170.5">15.5%</text><text x="480" y="170.5">6.5%</text>
        <text x="166" y="184">-0.1%</text><text x="271" y="184">-1.7%</text><text x="375" y="184">14.6%</text><text x="480" y="184">6.5%</text>
        <text x="166" y="197.5">7.2%</text><text x="271" y="197.5">4.6%</text><text x="375" y="197.5">5.7%</text><text x="480" y="197.5">5.2%</text>
        <text x="166" y="211">13.9%</text><text x="271" y="211">9.2%</text><text x="375" y="211">10.4%</text><text x="480" y="211">9.8%</text>
        <text x="166" y="224.5">-3.8%</text><text x="271" y="224.5">6.6%</text><text x="375" y="224.5">11.3%</text><text x="480" y="224.5">9.0%</text>
        <text x="166" y="238">19.3%</text><text x="271" y="238">7.7%</text><text x="375" y="238">10.7%</text><text x="480" y="238">9.2%</text>
        <text x="166" y="251.5">12.1%</text><text x="271" y="251.5">15.8%</text><text x="375" y="251.5">19.6%</text><text x="480" y="251.5">17.7%</text>
        <text x="166" y="265">2.5%</text><text x="271" y="265">8.2%</text><text x="375" y="265">5.1%</text><text x="480" y="265">6.7%</text>
      </g>
    </g>
  </svg>
  <p class="footnote" style="left:240px;top:282px">Benchmark = 45% xxxxxxxx, 15% yyyyyyyy, 40% zzzzzzzz</p>
</section>

<!-- Risk / return scatter -->
<section class="slide col-l r8">
  <span class="corner-mark"></span><span class="side-note">Private and Confidential – Not for Distribution</span><span class="page-no">15</span>
  <h2 class="slide-title">ABC, XYZ – Risk / Return vs Benchmark*</h2>
  <svg class="data-svg" viewBox="0 0 585 329" role="img" aria-label="Scatter chart of return against standard deviation">
    <g stroke="#eee"><line x1="84" y1="80" x2="523" y2="80"/><line x1="84" y1="102" x2="523" y2="102"/><line x1="84" y1="124" x2="523" y2="124"/><line x1="84" y1="146" x2="523" y2="146"/><line x1="84" y1="168" x2="523" y2="168"/><line x1="84" y1="190" x2="523" y2="190"/><line x1="84" y1="212" x2="523" y2="212"/><line x1="84" y1="234" x2="523" y2="234"/><line x1="84" y1="256" x2="523" y2="256"/></g>
    <g class="svg-text" font-size="5.5" fill="#888" text-anchor="end"><text x="80" y="82">16.0%</text><text x="80" y="104">14.0%</text><text x="80" y="126">12.0%</text><text x="80" y="148">10.0%</text><text x="80" y="170">8.0%</text><text x="80" y="192">6.0%</text><text x="80" y="214">4.0%</text><text x="80" y="236">2.0%</text><text x="80" y="258">0.0%</text></g>
    <g class="svg-text" font-size="5.5" fill="#888" text-anchor="middle"><text x="84" y="266">0.0%</text><text x="139" y="266">2.0%</text><text x="194" y="266">4.0%</text><text x="249" y="266">6.0%</text><text x="304" y="266">8.0%</text><text x="359" y="266">10.0%</text><text x="414" y="266">12.0%</text><text x="469" y="266">14.0%</text><text x="523" y="266">16.0%</text></g>
    <rect x="54" y="140" width="12" height="78" rx="6" fill="#7a7772"/>
    <text class="svg-text" transform="translate(62,179) rotate(-90)" font-size="6" fill="#fff" text-anchor="middle">Return</text>
    <rect x="248" y="273" width="74" height="11" rx="5.5" fill="#7a7772"/>
    <text class="svg-text" x="285" y="281" font-size="6" fill="#fff" text-anchor="middle">Standard Deviation</text>
    <g class="svg-text" font-size="5" fill="#555">
      <circle cx="196" cy="122" r="1.6" fill="#c0392b"/><text x="201" y="124">Delta Crest</text>
      <circle cx="163" cy="151" r="1.6" fill="#c0392b"/><text x="168" y="153">Hedge Funds 50/50</text>
      <circle cx="176" cy="181" r="1.6" fill="#222"/><text x="181" y="183">Harbor Point</text>
      <circle cx="143" cy="227" r="1.6" fill="#999"/><text x="148" y="229">Govt / Credit Bonds Index</text>
      <circle cx="311" cy="167" r="1.6" fill="#2a9d8f"/><text x="316" y="169">60/40 Benchmark</text>
      <circle cx="466" cy="106" r="1.6" fill="#2f6fb7"/><text x="455" y="94">Equity 3000</text>
      <circle cx="494" cy="201" r="1.6" fill="#2f6fb7"/><text x="438" y="190">Global ex US</text>
    </g>
  </svg>
  <p class="footnote" style="left:52px;top:294px">Benchmark = 45% xxxxxxxx, 15% yyyyyyyy, 40% zzzzzzzz</p>
</section>

<!-- Analytical data table -->
<section class="slide col-r r8">
  <span class="corner-mark"></span><span class="side-note">Private and Confidential – Not for Distribution</span><span class="page-no">16</span>
  <h2 class="slide-title">ABC, XYZ – analytical data vs Benchmark*</h2>
  <svg class="data-svg" viewBox="0 0 585 329" role="img" aria-label="Table of analytical statistics for 50/50 hedge funds versus benchmark">
    <rect x="43" y="88" width="397" height="27" fill="#7a7772"/>
    <rect x="440" y="88" width="103" height="27" fill="#8dc63f"/>
    <rect x="332" y="115" width="108" height="183" fill="#e6e6e6"/>
    <g class="svg-text" font-size="7" font-weight="600" fill="#fff" text-anchor="middle"><text x="386" y="99">50/50</text><text x="386" y="109">Hedge Funds</text><text x="491" y="104">Benchmark</text></g>
    <g class="svg-text" font-size="5.5" font-weight="700" fill="#222">
      <text x="47" y="124">Annualized Return</text><text x="47" y="137">Standard Deviation</text><text x="47" y="150">Average monthly return</text><text x="47" y="163">Largest monthly gain</text><text x="47" y="176">Largest monthly loss</text><text x="47" y="189">Max drawdown (consecutive negative months)</text><text x="47" y="202">% months of positive returns</text><text x="47" y="215">max # of months of consecutive loss</text><text x="47" y="228">Monthly standard deviation</text><text x="47" y="241">Min annual return with 99% probability</text><text x="47" y="254">% years outperformed 60/40 benchmark</text><text x="47" y="267">% months outperformed 60/40 benchmark</text><text x="47" y="280">R Square against benchmark</text>
    </g>
    <g class="svg-text" font-size="7" fill="#222" text-anchor="middle">
      <text x="386" y="124">9.5%</text><text x="491" y="124">8.1%</text>
      <text x="386" y="137">2.9%</text><text x="491" y="137">8.3%</text>
      <text x="386" y="150">0.8%</text><text x="491" y="150">0.7%</text>
      <text x="386" y="163">9.6%</text><text x="491" y="163">7.7%</text>
      <text x="386" y="176">-2.5%</text><text x="491" y="176">-8.6%</text>
      <text x="386" y="189">-2.5%</text><text x="491" y="189">-12.5%</text>
      <text x="386" y="202">86%</text><text x="491" y="202">72%</text>
      <text x="386" y="215">2 (twice)</text><text x="491" y="215">5 (once)</text>
      <text x="386" y="228">0.8%</text><text x="491" y="228">2.4%</text>
      <text x="386" y="241">3.7%</text><text x="491" y="241">-8.5%</text>
      <text x="386" y="254">60%</text>
      <text x="386" y="267">65%</text>
      <text x="386" y="280">8%</text><text x="491" y="280">100%</text>
    </g>
  </svg>
</section>

<!-- Monthly volatility -->
<section class="slide col-l r9">
  <span class="corner-mark"></span><span class="side-note">Private and Confidential – Not for Distribution</span><span class="page-no">17</span>
  <h2 class="slide-title" style="top:26px">ABC, XYZ vs Benchmark* – monthly volatility</h2>
  <span class="title-rule" style="top:58px"></span>
  <svg class="data-svg" viewBox="0 0 585 329" role="img" aria-label="Bar chart of monthly returns for ABC, XYZ and benchmark">
    <g stroke="#f0f0f0"><line x1="81" y1="93" x2="512" y2="93"/><line x1="81" y1="111" x2="512" y2="111"/><line x1="81" y1="129" x2="512" y2="129"/><line x1="81" y1="147" x2="512" y2="147"/><line x1="81" y1="165" x2="512" y2="165"/><line x1="81" y1="202" x2="512" y2="202"/><line x1="81" y1="220" x2="512" y2="220"/><line x1="81" y1="238" x2="512" y2="238"/><line x1="81" y1="256" x2="512" y2="256"/><line x1="81" y1="274" x2="512" y2="274"/></g>
    <line x1="81" y1="184" x2="512" y2="184" stroke="#bbb"/>
    <g class="svg-text" font-size="5" fill="#888" text-anchor="end"><text x="78" y="95">10.0%</text><text x="78" y="113">8.0%</text><text x="78" y="131">6.0%</text><text x="78" y="149">4.0%</text><text x="78" y="167">2.0%</text><text x="78" y="186">0.0%</text><text x="78" y="204">-2.0%</text><text x="78" y="222">-4.0%</text><text x="78" y="240">-6.0%</text><text x="78" y="258">-8.0%</text><text x="78" y="276">-10.0%</text></g>
    <path stroke="#2f6fb7" stroke-width="1.6" d="M92 184v-18M101 184v10M110 184v-25M119 184v-8M128 184v14M137 184v-30M146 184v-12M155 184v6M164 184v-20M173 184v22M182 184v-9M191 184v-15M200 184v8M209 184v-35M218 184v-5M227 184v12M236 184v-22M245 184v-14M254 184v30M263 184v-10M272 184v-6M281 184v-28M290 184v9M299 184v-16M308 184v18M317 184v-40M326 184v-8M335 184v5M344 184v-24M353 184v-12M362 184v15M371 184v-20M380 184v-9M389 184v70M398 184v-18M407 184v-11M416 184v-26M425 184v12M434 184v-7M443 184v-30M452 184v8M461 184v-15M470 184v-22M479 184v10M488 184v-12"/>
    <path stroke="#e98a2c" stroke-width="1.6" d="M95 184v-8M104 184v6M113 184v-12M122 184v4M131 184v9M140 184v-14M149 184v-5M158 184v8M167 184v-10M176 184v12M185 184v-4M194 184v-9M203 184v5M212 184v-16M221 184v-3M230 184v7M239 184v-11M248 184v-6M257 184v15M266 184v-5M275 184v-3M284 184v-13M293 184v6M302 184v-8M311 184v9M320 184v-18M329 184v-4M338 184v3M347 184v-12M356 184v-6M365 184v8M374 184v-10M383 184v-5M392 184v25M401 184v-9M410 184v-6M419 184v-13M428 184v6M437 184v-4M446 184v-15M455 184v4M464 184v-8M473 184v-11M482 184v5M491 184v-6"/>
    <g class="svg-text" font-size="4" fill="#999">
      <text transform="translate(95,196) rotate(-90)">Jan-10</text><text transform="translate(149,196) rotate(-90)">Jul-10</text><text transform="translate(203,196) rotate(-90)">Jan-11</text><text transform="translate(257,196) rotate(-90)">Jul-11</text><text transform="translate(311,196) rotate(-90)">Jan-12</text><text transform="translate(365,196) rotate(-90)">Jul-12</text><text transform="translate(419,196) rotate(-90)">Jan-13</text><text transform="translate(473,196) rotate(-90)">Jul-13</text>
    </g>
  </svg>
</section>

<!-- Return distribution -->
<section class="slide col-r r9">
  <span class="corner-mark"></span><span class="side-note">Private and Confidential – Not for Distribution</span><span class="page-no">18</span>
  <h2 class="slide-title" style="top:26px">ABC, XYZ – Return distribution</h2>
  <span class="title-rule" style="top:58px"></span>
  <svg class="data-svg" viewBox="0 0 585 329" role="img" aria-label="Histogram of ABC, XYZ monthly return distribution">
    <rect x="43" y="93" width="506" height="217" fill="#fff" stroke="#e4e4e4"/>
    <g class="svg-text" font-size="6" fill="#777" text-anchor="end"><text x="56" y="294">0</text><text x="56" y="274">5</text><text x="56" y="254">10</text><text x="56" y="234">15</text><text x="56" y="213">20</text><text x="56" y="193">25</text><text x="56" y="173">30</text><text x="56" y="153">35</text><text x="56" y="133">40</text><text x="56" y="112">45</text></g>
    <line x1="62" y1="292" x2="528" y2="292" stroke="#ccc"/>
    <g fill="#8dc63f" stroke="#fff" stroke-width="1">
      <rect x="62" y="288" width="38.8" height="4"/><rect x="100.8" y="288" width="38.8" height="4"/>
      <rect x="178.4" y="255.6" width="38.8" height="36.4"/><rect x="217.2" y="182.9" width="38.8" height="109.1"/>
      <rect x="256" y="134.4" width="38.8" height="157.6"/><rect x="294.8" y="158.7" width="38.8" height="133.3"/>
      <rect x="333.6" y="263.7" width="38.8" height="28.3"/><rect x="372.4" y="275.8" width="38.8" height="16.2"/>
      <rect x="489" y="288" width="38.8" height="4"/>
    </g>
    <g class="svg-text" font-size="3.8" fill="#888" text-anchor="middle"><text x="81" y="300">(-2.50%, -1.90%]</text><text x="120" y="300">(-1.90%, -1.30%]</text><text x="159" y="300">(-1.30%, -0.70%]</text><text x="198" y="300">(-0.70%, -0.10%]</text><text x="237" y="300">(-0.10%, 0.50%]</text><text x="275" y="300">(0.50%, 1.10%]</text><text x="314" y="300">(1.10%, 1.70%]</text><text x="353" y="300">(1.70%, 2.30%]</text><text x="392" y="300">(2.30%, 2.90%]</text><text x="431" y="300">(2.90%, 3.50%]</text><text x="469" y="300">(3.50%, 4.10%]</text><text x="508" y="300">(4.10%, 4.70%]</text></g>
  </svg>
</section>

<!-- Benchmark distribution -->
<section class="slide col-l r10">
  <span class="corner-mark"></span><span class="side-note">Private and Confidential – Not for Distribution</span><span class="page-no">19</span>
  <h2 class="slide-title" style="top:26px">Benchmark* – Return distribution</h2>
  <span class="title-rule" style="top:58px"></span>
  <svg class="data-svg" viewBox="0 0 585 329" role="img" aria-label="Histogram of benchmark monthly return distribution">
    <g class="svg-text" font-size="5.5" fill="#777" text-anchor="end"><text x="64" y="271">0</text><text x="64" y="243">10</text><text x="64" y="214">20</text><text x="64" y="186">30</text><text x="64" y="157">40</text><text x="64" y="129">50</text><text x="64" y="100">60</text></g>
    <line x1="68" y1="269" x2="536" y2="269" stroke="#ccc"/>
    <g fill="#8dc63f" stroke="#fff" stroke-width="1">
      <rect x="68" y="267.6" width="46.8" height="1.4"/><rect x="114.8" y="267.6" width="46.8" height="1.4"/>
      <rect x="161.6" y="257.6" width="46.8" height="11.4"/><rect x="208.4" y="259" width="46.8" height="10"/>
      <rect x="255.2" y="206.3" width="46.8" height="62.7"/><rect x="302" y="112.3" width="46.8" height="156.7"/>
      <rect x="348.8" y="203.5" width="46.8" height="65.5"/><rect x="395.6" y="256.2" width="46.8" height="12.8"/>
      <rect x="442.4" y="267.6" width="46.8" height="1.4"/><rect x="489.2" y="261.9" width="46.8" height="7.1"/>
    </g>
    <g class="svg-text" font-size="3.8" fill="#888" text-anchor="middle"><text x="91" y="278">(-8.40%, -6.90%]</text><text x="138" y="278">(-6.90%, -5.30%]</text><text x="185" y="278">(-5.30%, -3.70%]</text><text x="232" y="278">(-3.70%, -2.10%]</text><text x="279" y="278">(-2.10%, -0.50%]</text><text x="325" y="278">(-0.50%, 1.00%]</text><text x="372" y="278">(1.00%, 2.60%]</text><text x="419" y="278">(2.60%, 4.20%]</text><text x="466" y="278">(4.20%, 5.70%]</text><text x="513" y="278">(5.70%, 7.30%]</text></g>
  </svg>
</section>

<!-- Disclaimer -->
<section class="slide col-r r10">
  <span class="corner-mark"></span><span class="side-note">Private and Confidential – Not for Distribution</span><span class="page-no">20</span>
  <h2 class="disc-title">Disclaimer</h2>
  <p class="disc-body">Disclaimer: this document is a general communication being provided for informational purposes only. It is educational in nature and not designed to be taken as advice or a recommendation for any specific investment product, strategy, plan feature or other purpose in any jurisdiction. Any examples used are generic, hypothetical and for illustration purposes only. This material does not contain sufficient information to support an investment decision and it should not be relied upon by you in evaluating the merits of investing in any securities or products. In addition, users should make an independent assessment of the legal, regulatory, tax, credit, and accounting implications and determine, together with their own professional advisers, if any investment mentioned herein is believed to be suitable to their personal goals. Investors should ensure that they obtain all available relevant information before making any investment. Any forecasts, figures, opinions or investment techniques and strategies set out are for information purposes only, based on certain assumptions and current market conditions and are subject to change without prior notice. All information presented herein is considered to be accurate at the time of production, but no warranty of accuracy is given and no liability in respect of any error or omission is accepted. It should be noted that investment involves risks, the value of investments and the income from them may fluctuate in accordance with market conditions and taxation agreements and investors may not get back the full amount invested. Both past performance and yields are not reliable indicators of current and future results.</p>
</section>

</main>
</body>
</html>
```